Business Card Design for New Game Studio

We need a business card design. We are a new company developing innovative mobile and platform games.

I would like to see very innovative design thats brings out the company's goal and direction.

My Company's goal and direction is to "Evolve the way of gaming, Bring fun and entertainment to all gamers"

Please do use our company logo which I have attached to be included in the design.

Please put in details for name, title, contacts etc ... be creative !!!

Reason: Company logo redesign. Awaiting it. Thanks

Hi all Please do wait for my updated company logo. Thanks

Reason: Still waiting on new company logo. Thanks all

Hi All Designers .... Sorry for the long wait... Please see the new file for my new company logo uploaded. Waiting to see all your creative design. Cheers

Hi All .... Please do not just mass send a whole bunch of similar designs .... Would like to see quality instead of quantity Cheers

Entertainment

```html
<!DOCTYPE html>
<html lang="en">
<head>
<meta charset="utf-8">
<title>Nova Keep Games – Business Card</title>
<link rel="stylesheet" href="https://fonts.googleapis.com/css2?family=Open+Sans:wght@400;600;700&display=swap">
<style>
  :root {
    --stage: #3a3a3c;
    --card-black: #1d1d1f;
    --card-dark: #262629;
    --lime: #8fe03a;
    --lime-deep: #3cae2c;
    --teal: #1f5f66;
    --white: #ffffff;
    --soft-grey: #c9c9c9;
  }
  * { box-sizing: border-box; margin: 0; padding: 0; }
  html, body {
    width: 1200px; height: 776px; overflow: hidden;
    background: var(--stage);
    font-family: "Open Sans", Arial, sans-serif;
  }
  .stage {
    position: relative; width: 1200px; height: 776px;
    display: flex; align-items: center; justify-content: center; gap: 60px;
  }
  .card {
    position: relative; width: 500px; height: 286px;
    border-radius: 4px; overflow: hidden;
    box-shadow: 0 14px 30px rgba(0,0,0,.45);
  }
  .card svg.card-art { position: absolute; inset: 0; width: 100%; height: 100%; }

  .brand { display: flex; align-items: center; }
  .brand-dot { border-radius: 50%; flex: none; }
  .brand-name { font-weight: 700; letter-spacing: 1px; text-transform: uppercase; white-space: nowrap; }

  /* Back side */
  .card-back { background: var(--card-black); }
  .back-brand {
    position: absolute; left: 0; right: 0; top: 116px;
    justify-content: center; gap: 12px;
  }
  .back-brand .brand-dot { width: 22px; height: 22px; background: var(--lime); }
  .back-brand .brand-name { font-size: 28px; color: var(--lime); }
  .back-web {
    position: absolute; left: 22px; bottom: 58px;
    font-size: 13px; font-weight: 600; color: var(--lime);
  }

  /* Front side */
  .card-front { background: var(--card-dark); }
  .front-brand { position: absolute; left: 22px; top: 36px; gap: 8px; }
  .front-brand .brand-dot { width: 16px; height: 16px; background: var(--card-black); }
  .front-brand .brand-name { font-size: 19px; color: var(--card-black); }
  .contact {
    position: absolute; right: 26px; top: 112px; text-align: right;
    color: var(--white);
  }
  .contact-name { font-weight: 700; font-size: 16px; letter-spacing: .5px; }
  .contact-title { font-size: 10px; color: var(--lime); margin-bottom: 14px; }
  .contact-line {
    display: flex; align-items: center; justify-content: flex-end; gap: 8px;
    font-size: 11.5px; color: var(--soft-grey); line-height: 19px; white-space: nowrap;
  }
  .contact-line svg, .icon-gap { width: 10px; height: 10px; flex: none; }
</style>
</head>
<body>
<main class="stage">

  <section class="card card-back" aria-label="Business card back">
    <svg class="card-art" viewBox="0 0 500 286" aria-hidden="true">
      <rect x="0" y="0" width="500" height="10" fill="var(--lime-deep)"/>
      <rect x="380" y="196" width="120" height="56" fill="var(--lime)"/>
    </svg>
    <div class="brand back-brand">
      <span class="brand-dot"></span>
      <span class="brand-name">Nova Keep Games</span>
    </div>
    <p class="back-web">www.novakeepgames.com</p>
  </section>

  <section class="card card-front" aria-label="Business card front">
    <svg class="card-art" viewBox="0 0 500 286" aria-hidden="true">
      <defs>
        <linearGradient id="lime-fade" x1="0" y1="0" x2="1" y2="0">
          <stop offset="0" stop-color="var(--lime-deep)"/>
          <stop offset="1" stop-color="var(--lime)"/>
        </linearGradient>
      </defs>
      <path d="M0,0 H500 V70 Q250,60 0,200 Z" fill="url(#lime-fade)"/>
      <path d="M0,200 Q250,60 500,70" stroke="var(--white)" stroke-width="4" fill="none"/>
      <rect x="0" y="278" width="500" height="8" fill="var(--teal)"/>
    </svg>
    <div class="brand front-brand">
      <span class="brand-dot"></span>
      <span class="brand-name">Nova Keep Games</span>
    </div>
    <div class="contact">
      <p class="contact-name">ALEX MARLOW</p>
      <p class="contact-title">Manager</p>
      <p class="contact-line">+ 000 - 2468 - 1357
        <svg viewBox="0 0 10 10"><path d="M2,1 L4,1 L5,3 L4,4 C4.5,5.5 5,6 6,6.5 L7,5.5 L9,6.5 L9,8.5 C5,9 1,5 2,1 Z" fill="var(--lime)"/></svg>
      </p>
      <p class="contact-line">42 Harbor Lane,
        <svg viewBox="0 0 10 10"><path d="M5,0.5 C3,0.5 1.8,2 1.8,3.7 C1.8,6 5,9.5 5,9.5 C5,9.5 8.2,6 8.2,3.7 C8.2,2 7,0.5 5,0.5 Z" fill="var(--lime)"/><circle cx="5" cy="3.7" r="1.2" fill="var(--card-dark)"/></svg>
      </p>
      <p class="contact-line">Port Ellis 60218 <span class="icon-gap"></span></p>
      <p class="contact-line">hello@novakeepgames.com
        <svg viewBox="0 0 10 10"><rect x="0.5" y="2" width="9" height="6" fill="var(--lime)"/><path d="M0.5,2 L5,5.5 L9.5,2" stroke="var(--card-dark)" fill="none"/></svg>
      </p>
    </div>
  </section>

</main>
</body>
</html>
```